Business Card Design

We sell fish products to corporate food companies who then turn these products into final food products for consumers

Industry/Entity Type

Business

Contact Information for Business Card

I need a corporate business card template for a fish products business. We would like it be professional for use in dealing with multi national companies. This company business card template will be used by multiple employees so the following fields must be open to edit (Name, Phone Number and Email address)

```html
<!DOCTYPE html>
<html lang="en">
<head>
<meta charset="utf-8">
<title>Tidewater Seafoods – Business Card</title>
<link rel="stylesheet" href="https://fonts.googleapis.com/css2?family=Open+Sans:wght@400;600&display=swap">
<style>
  :root {
    --page-bg: #2a1416;
    --card-white: #ffffff;
    --card-black: #0d0d0d;
    --brand-blue: #1a5fae;
    --accent-teal: #1fb5d6;
    --text-light: #e6e6e6;
    --divider: #8a8a8a;
  }
  * { margin: 0; padding: 0; box-sizing: border-box; }
  html, body {
    width: 1200px; height: 800px; overflow: hidden;
    background: var(--page-bg);
    font-family: "Open Sans", Arial, sans-serif;
  }
  .canvas {
    position: relative; width: 1200px; height: 800px;
    display: flex; align-items: center; justify-content: center;
  }
  .card {
    position: relative; width: 900px; height: 514px;
    overflow: hidden; box-shadow: 0 20px 50px rgba(0,0,0,.5);
  }
  .card-bg { position: absolute; inset: 0; }
  .brand {
    position: absolute; left: 250px; top: 118px;
    display: flex; align-items: center; gap: 14px;
    white-space: nowrap;
  }
  .brand-dot {
    width: 48px; height: 48px; border-radius: 50%;
    background: var(--brand-blue);
  }
  .brand-name {
    font-weight: 600; font-size: 38px; line-height: 1.2;
    color: var(--brand-blue); letter-spacing: .3px;
  }
  .holder {
    position: absolute; left: 190px; top: 378px; text-align: right;
  }
  .holder-name {
    font-weight: 600; font-size: 34px; color: var(--accent-teal); line-height: 1.1;
  }
  .holder-role {
    font-size: 17px; color: var(--text-light);
  }
  .divider {
    position: absolute; left: 482px; top: 318px; width: 1px; height: 150px;
    background: var(--divider);
  }
  .contacts {
    position: absolute; left: 505px; top: 318px; list-style: none;
    color: var(--text-light); font-size: 17px; line-height: 26px;
  }
  .contacts li { display: flex; align-items: flex-start; gap: 10px; }
  .contacts svg { flex: 0 0 18px; width: 18px; height: 18px; margin-top: 4px; fill: var(--accent-teal); }
</style>
</head>
<body>
<main class="canvas">
  <article class="card">
    <svg class="card-bg" viewBox="0 0 900 514" width="900" height="514" aria-hidden="true">
      <defs>
        <linearGradient id="wave-line" x1="0" x2="1" y1="0" y2="0">
          <stop offset="0" stop-color="#1a5fae"/>
          <stop offset=".5" stop-color="#1fb5d6"/>
          <stop offset="1" stop-color="#1a5fae"/>
        </linearGradient>
        <linearGradient id="black-fade" x1="0" y1="0" x2="0" y2="1">
          <stop offset="0" stop-color="#1a1a1a"/>
          <stop offset="1" stop-color="#050505"/>
        </linearGradient>
      </defs>
      <rect width="900" height="514" fill="#ffffff"/>
      <path d="M0,300 C220,370 560,330 900,70 L900,514 L0,514 Z" fill="url(#black-fade)"/>
      <path d="M0,300 C220,370 560,330 900,70" fill="none" stroke="url(#wave-line)" stroke-width="5"/>
    </svg>

    <div class="brand">
      <span class="brand-dot"></span>
      <span class="brand-name">Tidewater Seafoods</span>
    </div>

    <div class="holder">
      <p class="holder-name">Daniel Reyes</p>
      <p class="holder-role">manager</p>
    </div>

    <div class="divider"></div>

    <ul class="contacts">
      <li>
        <svg viewBox="0 0 24 24"><path d="M6.6 10.8a15 15 0 0 0 6.6 6.6l2.2-2.2c.3-.3.7-.4 1-.2 1.1.4 2.3.6 3.6.6.6 0 1 .4 1 1V20c0 .6-.4 1-1 1C10.6 21 3 13.4 3 4c0-.6.4-1 1-1h3.5c.6 0 1 .4 1 1 0 1.3.2 2.5.6 3.6.1.3 0 .7-.2 1z"/></svg>
        <span>0412555019</span>
      </li>
      <li>
        <svg viewBox="0 0 24 24"><path d="M3 5h18v14H3z M3 5l9 7 9-7" fill="none" stroke="#1fb5d6" stroke-width="2"/></svg>
        <span>sam@harbourlinetrade.com</span>
      </li>
      <li>
        <svg viewBox="0 0 24 24"><circle cx="12" cy="12" r="9" fill="none" stroke="#1fb5d6" stroke-width="2"/><path d="M3 12h18M12 3c3 3 3 15 0 18M12 3c-3 3-3 15 0 18" fill="none" stroke="#1fb5d6" stroke-width="1.6"/></svg>
        <span>www.harbourlinetrade.com</span>
      </li>
      <li>
        <svg viewBox="0 0 24 24"><path d="M12 3l9 8h-3v9h-4v-6h-4v6H6v-9H3z"/></svg>
        <span>Unit 12, Northgate Trade Park<br>Salem, OR</span>
      </li>
    </ul>
  </article>
</main>
</body>
</html>
```